Business Card - Professional Minimalist - Double sided

We appreciate minimalist logo/web/collateral designs that allow design to tell a story. We want to relay a professional image/approach but throwing in a splash of modern when we’re able so long as it’s not distracting. Think 75% classic corporate, 25% modern. Open to black or white design, not sure which might look the best.

Target Market(s)

Senior executives or related government affairs contacts within the agriculture, energy, and defense industries (i.e., potential clients) but located outside of Washington, DC. Most potential clients based in DC with be familiar with both of us and our shared history.

Industry/Entity Type

Consulting

Contact Information for Business Card

Name: Daniel R. Whitlock
Title: Co-Founder & Partner
Address: 418 Bramblewood Ave. SE | Suite 2716 | Washington, D.C. 20019
Phone: (202) 555-0187
Email: Daniel@HollerbyWhitlock.com

Font styles to use
Serif

Colors

Designer to choose only greyscale colors for use in the design.

Requirements
Must have
• Name: Daniel R. Whitlock
Phone: (202) 555-0187

```html
<!DOCTYPE html>
<html lang="en">
<head>
<meta charset="utf-8">
<title>Hollerby Whitlock Group – Business Card</title>
<link href="https://fonts.googleapis.com/css2?family=Marcellus&family=Montserrat:wght@400;500&display=swap" rel="stylesheet">
<style>
  :root {
    --page: #ececec;
    --card-dark: #58595b;
    --card-light: #ffffff;
    --ink: #58595b;
    --ink-soft: #6d6e70;
    --rule: #9a9b9d;
    --on-dark: #ffffff;
  }
  * { box-sizing: border-box; margin: 0; padding: 0; }
  html, body { width: 1200px; height: 883px; overflow: hidden; }
  body {
    background: var(--page);
    font-family: "Montserrat", sans-serif;
    display: flex;
    align-items: center;
    justify-content: center;
    gap: 44px;
  }
  .card {
    position: relative;
    width: 520px;
    height: 297px;
    box-shadow: 0 6px 18px rgba(0,0,0,0.12);
  }
  .card--front { background: var(--card-dark); color: var(--on-dark); }
  .card--back { background: var(--card-light); color: var(--ink); }

  .wordmark {
    font-family: "Marcellus", serif;
    font-weight: 400;
    text-transform: uppercase;
    letter-spacing: 0.04em;
    white-space: nowrap;
  }
  .card--front .wordmark {
    position: absolute;
    left: 0; right: 0; top: 100px;
    text-align: center;
    font-size: 27px;
  }
  .card--front .wordmark-rule {
    position: absolute;
    left: 150px; right: 150px; top: 146px;
    height: 1px; background: rgba(255,255,255,0.6);
  }
  .card--front .site {
    position: absolute;
    left: 0; right: 0; bottom: 44px;
    text-align: center;
    font-size: 12px;
    letter-spacing: 0.03em;
  }

  .card--back .wordmark {
    position: absolute;
    right: 38px; top: 44px;
    font-size: 21px;
    color: var(--ink);
  }
  .card--back .wordmark-rule {
    position: absolute;
    right: 38px; width: 220px; top: 78px;
    height: 1px; background: var(--rule);
  }
  .divider {
    position: absolute;
    left: 28px; right: 28px; top: 186px;
    height: 1px; background: var(--rule);
  }
  .person {
    position: absolute;
    left: 28px; bottom: 118px;
  }
  .person-name {
    font-family: "Marcellus", serif;
    font-size: 22px;
    text-transform: uppercase;
    letter-spacing: 0.02em;
    line-height: 1.1;
  }
  .person-title { font-size: 11.5px; color: var(--ink-soft); margin-top: 3px; }
  .address {
    position: absolute;
    right: 38px; bottom: 118px;
    text-align: right;
    font-size: 11px;
    line-height: 1.45;
    color: var(--ink-soft);
  }
  .contacts {
    position: absolute;
    left: 34px; top: 200px;
    list-style: none;
    font-size: 11.5px;
    line-height: 1;
    color: var(--ink-soft);
  }
  .contacts li { display: flex; align-items: center; gap: 7px; height: 20px; }
  .contacts svg { width: 11px; height: 11px; fill: var(--ink); flex: none; }
</style>
</head>
<body>
  <section class="card card--front" aria-label="Card front">
    <div class="wordmark">Hollerby Whitlock Group</div>
    <div class="wordmark-rule"></div>
    <div class="site">www.HollerbyWhitlock.com</div>
  </section>

  <section class="card card--back" aria-label="Card back">
    <div class="wordmark">Hollerby Whitlock Group</div>
    <div class="wordmark-rule"></div>

    <div class="person">
      <div class="person-name">Daniel R. Whitlock</div>
      <div class="person-title">Co-Founder &amp; Partner</div>
    </div>

    <address class="address" style="font-style:normal">
      418 Bramblewood Ave. SE<br>
      Suite 2716<br>
      Washington, D.C. 20019
    </address>

    <div class="divider"></div>

    <ul class="contacts">
      <li>
        <svg viewBox="0 0 12 12" aria-hidden="true"><path d="M1 4.5C1 3 3 2 6 2s5 1 5 2.5V5H8.5V4H3.5v1H1zM3 5.5h6l1.5 5h-9z"/></svg>
        (202) 555-0187
      </li>
      <li>
        <svg viewBox="0 0 12 12" aria-hidden="true"><path d="M1 2.5h10v7H1zM1.6 3.1 6 6.6l4.4-3.5v-.1H1.6z"/></svg>
        Daniel@HollerbyWhitlock.com
      </li>
      <li>
        <svg viewBox="0 0 12 12" aria-hidden="true"><circle cx="6" cy="6" r="5"/><path d="M3 4.5h2.5v2H3zM6.5 7h2.5v2H6.5z" fill="#fff"/></svg>
        www.HollerbyWhitlock.com
      </li>
    </ul>
  </section>
</body>
</html>
```